Nectarine Point of Sale Cards for Grocery Retail Markets

We are looking to update our Nectarine point of sale card and price card. The cards will need to be 7" x 11" with a .125 bleed - one sided. See attached for the old versions. We would like this to use photos that look like true Washington State Peaches. Here are the bullet points we would like to use: - New Crop!- Tree Ripened- Excellent FlavorNOTE: The price card just needs to have a space where a retailer can write in the sale price of the item. See attachment with the white box.

Target Market(s)

Retail market shoppers

Requirements
Must have
• Pictures of Nectarines Only

```html
<!DOCTYPE html>
<html lang="en">
<head>
<meta charset="utf-8">
<title>Nectarine Point of Sale and Price Cards</title>
<link rel="stylesheet" href="https://fonts.googleapis.com/css2?family=Encode+Sans+Semi+Condensed:wght@600&family=Montserrat:ital,wght@0,900;1,900&family=Nunito:wght@800&display=swap">
<style>
  :root {
    --page-bg: #efeae2;
    --card-white: #ffffff;
    --banner-red: #a51f22;
    --banner-orange: #f04e12;
    --headline-yellow: #f9e900;
    --leaf-green: #8dc63f;
    --bullet-green: #7dc242;
    --brand-green: #1d6b38;
    --price-green: #0f8a2e;
    --fruit-deep: #9e1414;
    --fruit-red: #d8231a;
    --fruit-orange: #f2661c;
    --fruit-gold: #f8c23a;
    --fruit-blush: #f6a27c;
  }
  * { margin: 0; padding: 0; box-sizing: border-box; }
  html, body {
    width: 994px;
    height: 1200px;
    overflow: hidden;
    background: var(--page-bg);
  }
  .sheet { position: relative; width: 994px; height: 1200px; }
  .card {
    position: absolute;
    left: 100px;
    width: 794px;
    height: 508px;
    background: var(--card-white);
    overflow: hidden;
    box-shadow: 0 6px 18px rgba(0,0,0,0.2);
  }
  .card--display { top: 68px; }
  .card--price { top: 626px; }
  .card-art { position: absolute; inset: 0; width: 794px; height: 508px; }
  .headline {
    font-family: "Encode Sans Semi Condensed", "Arial Narrow", sans-serif;
    font-weight: 600;
    font-size: 45px;
    fill: var(--headline-yellow);
  }
  .selling-points {
    position: absolute;
    left: 148px;
    top: 160px;
    list-style: none;
  }
  .selling-points li {
    position: relative;
    padding-left: 28px;
    height: 58px;
    font-family: "Montserrat", "Arial Black", sans-serif;
    font-style: italic;
    font-weight: 900;
    font-size: 48px;
    line-height: 58px;
    letter-spacing: -0.5px;
    color: #ffffff;
    text-shadow: 2px 3px 4px rgba(0,0,0,0.6);
    white-space: nowrap;
  }
  .selling-points li::before {
    content: "";
    position: absolute;
    left: 0;
    top: 22px;
    width: 15px;
    height: 15px;
    border-radius: 50%;
    background: var(--bullet-green);
  }
  .brand {
    position: absolute;
    left: 20px;
    top: 438px;
    display: flex;
    align-items: center;
    gap: 14px;
  }
  .brand-mark {
    width: 62px;
    height: 62px;
    border-radius: 50%;
    background: var(--fruit-orange);
  }
  .brand-name {
    font-family: "Nunito", "Arial", sans-serif;
    font-weight: 800;
    font-size: 19px;
    line-height: 19px;
    color: var(--brand-green);
  }
  .price-symbol {
    position: absolute;
    left: 502px;
    top: 388px;
    font-family: "Montserrat", "Arial Black", sans-serif;
    font-weight: 900;
    font-size: 84px;
    line-height: 90px;
    color: var(--price-green);
  }
</style>
</head>
<body>
<main class="sheet">

  <section class="card card--display">
    <svg class="card-art" viewBox="0 0 794 508" xmlns="http://www.w3.org/2000/svg">
      <defs>
        <linearGradient id="d-green" x1="0" y1="0" x2="1" y2="0">
          <stop offset="0" stop-color="#ffffff"/>
          <stop offset="0.6" stop-color="var(--leaf-green)"/>
          <stop offset="1" stop-color="#93c83a"/>
        </linearGradient>
        <radialGradient id="d-cluster" cx="0.3" cy="0.75" r="0.95">
          <stop offset="0" stop-color="var(--fruit-red)"/>
          <stop offset="0.3" stop-color="#c9281f"/>
          <stop offset="0.5" stop-color="var(--fruit-orange)"/>
          <stop offset="0.72" stop-color="var(--fruit-blush)"/>
          <stop offset="1" stop-color="#ffffff"/>
        </radialGradient>
        <radialGradient id="d-fruit" cx="0.6" cy="0.12" r="0.95">
          <stop offset="0" stop-color="var(--fruit-gold)"/>
          <stop offset="0.22" stop-color="#f58a24"/>
          <stop offset="0.5" stop-color="var(--fruit-red)"/>
          <stop offset="1" stop-color="var(--fruit-deep)"/>
        </radialGradient>
        <linearGradient id="d-footer" x1="0" y1="0" x2="1" y2="0">
          <stop offset="0" stop-color="#ffffff"/>
          <stop offset="0.6" stop-color="#ffffff"/>
          <stop offset="1" stop-color="var(--leaf-green)"/>
        </linearGradient>
        <linearGradient id="d-banner" x1="0" y1="0" x2="1" y2="0">
          <stop offset="0" stop-color="var(--banner-red)"/>
          <stop offset="0.3" stop-color="var(--banner-orange)"/>
          <stop offset="0.7" stop-color="var(--banner-orange)"/>
          <stop offset="1" stop-color="var(--banner-red)"/>
        </linearGradient>
        <filter id="d-soft" x="-5%" y="-5%" width="110%" height="110%">
          <feDropShadow dx="-3" dy="4" stdDeviation="5" flood-opacity="0.3"/>
        </filter>
        <filter id="d-type" x="-5%" y="-20%" width="110%" height="140%">
          <feDropShadow dx="1" dy="2" stdDeviation="1.5" flood-opacity="0.45"/>
        </filter>
        <path id="d-arc" d="M22 87 Q 396 33 770 87"/>
      </defs>
      <rect class="leaf-backdrop" x="420" y="0" width="374" height="420" fill="url(#d-green)"/>
      <rect class="photo-cluster" role="img" aria-label="Photo of a pile of ripe red and yellow nectarines" x="0" y="80" width="540" height="338" fill="url(#d-cluster)"/>
      <rect class="footer-strip" x="0" y="418" width="560" height="90" fill="url(#d-footer)"/>
      <path class="photo-feature" role="img" aria-label="Photo of a single large nectarine with stem and leaves" filter="url(#d-soft)" d="M460 508 C 418 450 404 360 424 300 C 454 200 560 132 662 132 C 726 132 776 150 794 170 L794 508 Z" fill="url(#d-fruit)"/>
      <path class="banner" d="M0 44 Q 396 -20 794 40 L794 112 Q 396 56 0 112 Z" fill="url(#d-banner)"/>
      <text class="headline" filter="url(#d-type)"><textPath href="#d-arc" textLength="745" lengthAdjust="spacingAndGlyphs">Proud Nectarines from Washington State</textPath></text>
    </svg>
    <ul class="selling-points">
      <li>New Crop!</li>
      <li>Tree Ripened</li>
      <li>Excellent Flavor</li>
    </ul>
    <div class="brand">
      <span class="brand-mark"></span>
      <p class="brand-name">Cascade Orchard<br>Growers Council</p>
    </div>
  </section>

  <section class="card card--price">
    <svg class="card-art" viewBox="0 0 794 508" xmlns="http://www.w3.org/2000/svg">
      <defs>
        <linearGradient id="p-green" x1="0" y1="0" x2="1" y2="0">
          <stop offset="0" stop-color="#ffffff"/>
          <stop offset="0.6" stop-color="var(--leaf-green)"/>
          <stop offset="1" stop-color="#93c83a"/>
        </linearGradient>
        <radialGradient id="p-cluster" cx="0.3" cy="0.75" r="0.95">
          <stop offset="0" stop-color="var(--fruit-red)"/>
          <stop offset="0.3" stop-color="#c9281f"/>
          <stop offset="0.5" stop-color="var(--fruit-orange)"/>
          <stop offset="0.72" stop-color="var(--fruit-blush)"/>
          <stop offset="1" stop-color="#ffffff"/>
        </radialGradient>
        <radialGradient id="p-fruit" cx="0.6" cy="0.12" r="0.95">
          <stop offset="0" stop-color="var(--fruit-gold)"/>
          <stop offset="0.22" stop-color="#f58a24"/>
          <stop offset="0.5" stop-color="var(--fruit-red)"/>
          <stop offset="1" stop-color="var(--fruit-deep)"/>
        </radialGradient>
        <linearGradient id="p-footer" x1="0" y1="0" x2="1" y2="0">
          <stop offset="0" stop-color="#ffffff"/>
          <stop offset="0.6" stop-color="#ffffff"/>
          <stop offset="1" stop-color="var(--leaf-green)"/>
        </linearGradient>
        <linearGradient id="p-banner" x1="0" y1="0" x2="1" y2="0">
          <stop offset="0" stop-color="var(--banner-red)"/>
          <stop offset="0.3" stop-color="var(--banner-orange)"/>
          <stop offset="0.7" stop-color="var(--banner-orange)"/>
          <stop offset="1" stop-color="var(--banner-red)"/>
        </linearGradient>
        <filter id="p-soft" x="-5%" y="-5%" width="110%" height="110%">
          <feDropShadow dx="-3" dy="4" stdDeviation="5" flood-opacity="0.3"/>
        </filter>
        <filter id="p-type" x="-5%" y="-20%" width="110%" height="140%">
          <feDropShadow dx="1" dy="2" stdDeviation="1.5" flood-opacity="0.45"/>
        </filter>
        <path id="p-arc" d="M22 87 Q 396 33 770 87"/>
      </defs>
      <rect class="leaf-backdrop" x="420" y="0" width="374" height="420" fill="url(#p-green)"/>
      <rect class="photo-cluster" role="img" aria-label="Photo of a pile of ripe red and yellow nectarines" x="0" y="80" width="540" height="338" fill="url(#p-cluster)"/>
      <rect class="footer-strip" x="0" y="418" width="560" height="90" fill="url(#p-footer)"/>
      <path class="photo-feature" role="img" aria-label="Photo of a single large nectarine with stem and leaves" filter="url(#p-soft)" d="M460 508 C 418 450 404 360 424 300 C 454 200 560 132 662 132 C 726 132 776 150 794 170 L794 508 Z" fill="url(#p-fruit)"/>
      <path class="price-box" d="M472 362 L794 362 L794 508 L472 508 L496 414 Z" fill="#ffffff"/>
      <path class="banner" d="M0 44 Q 396 -20 794 40 L794 112 Q 396 56 0 112 Z" fill="url(#p-banner)"/>
      <text class="headline" filter="url(#p-type)"><textPath href="#p-arc" textLength="745" lengthAdjust="spacingAndGlyphs">Proud Nectarines from Washington State</textPath></text>
    </svg>
    <ul class="selling-points">
      <li>New Crop!</li>
      <li>Tree Ripened</li>
      <li>Excellent Flavor</li>
    </ul>
    <span class="price-symbol">$</span>
    <div class="brand">
      <span class="brand-mark"></span>
      <p class="brand-name">Cascade Orchard<br>Growers Council</p>
    </div>
  </section>

</main>
</body>
</html>
```